Business card, Invoice and printable service brochure

I need a 5.5x8.5 invoice, business card and printable service template for reception desk designed for my Rug repair, restoration and cleaning business.

I have included a picture for reference

www.belkarrug.com

Columns i need in my invoice:
Type of rug, Size, Background Color, Repair needs, Notes, Price and rug cleaning disclaimer.

Target Market(s)

Higher segment clients

Industry/Entity Type

Rug Repair, Restoration and cleaning,

Requirements
Must have
• Services hast to be listed on the invoice as well as service brochure.

```html
<!DOCTYPE html>
<html lang="en">
<head>
<meta charset="utf-8">
<title>Belkar Rug — Invoice and Business Card</title>
<link href="https://fonts.googleapis.com/css2?family=Heebo:wght@300;400;500;700&display=swap" rel="stylesheet">
<style>
:root{
  --backdrop:#86cfee;
  --navy:#17294a;
  --navy-deep:#121f3a;
  --gold:#cc9200;
  --gold-soft:#c9a565;
  --row-a:#dcdce0;
  --row-b:#ececef;
  --ink:#1c1c1c;
  --muted:#555;
  --white:#fff;
}
*{margin:0;padding:0;box-sizing:border-box}
html,body{width:1200px;height:1200px;overflow:hidden}
body{background:var(--backdrop);font-family:'Heebo',sans-serif;color:var(--ink);position:relative}
.abs{position:absolute;white-space:nowrap}

/* name set in the text font, single colour and weight */
.brand-name{font-family:'Heebo',sans-serif;font-weight:500;color:var(--gold-soft);letter-spacing:2px;line-height:1}

/* invoice */
.invoice{position:absolute;left:68px;top:90px;width:674px;height:963px;background:var(--white);box-shadow:0 20px 50px rgba(10,40,90,.35);overflow:hidden}
.invoice-header{position:absolute;left:0;top:0;width:100%;height:94px;background:var(--navy-deep);display:flex;align-items:center;justify-content:center}
.invoice-header .brand-name{font-size:40px}

.invoice-badge{left:444px;top:155px;width:165px;height:44px;background:var(--gold);color:var(--white);font-weight:700;font-size:30px;letter-spacing:1px;text-align:center;line-height:44px}
.invoice-to{left:58px;top:172px;font-size:15px;font-weight:400}
.customer-bar{left:52px;top:200px;width:558px;height:25px;background:var(--navy);color:var(--white)}
.customer-bar .label{position:absolute;left:6px;top:0;line-height:25px;font-weight:700;font-size:16px}
.customer-bar .number{position:absolute;left:428px;top:0;line-height:25px;font-size:14px}
.customer-details{left:58px;top:233px;font-size:10px;line-height:12.5px}
.meta{font-size:12px;line-height:15px}

.items-head{left:52px;top:326px;width:622px;height:42px;background:var(--gold);color:var(--white);font-size:15px;font-weight:300}
.items-head span,.item-row span{position:absolute;top:0}
.items-head span{line-height:42px}
.item-row{position:absolute;left:0;width:674px;height:34px;font-size:16px;font-weight:300}
.item-row:nth-child(odd){background:var(--row-a)}
.item-row:nth-child(even){background:var(--row-b)}
.item-row span{line-height:34px}
.c-id{left:70px}.c-item{left:114px}.c-price{left:358px}.c-qty{left:481px}.c-total{left:562px}
.items-head .h-id{left:18px}.items-head .h-item{left:65px}.items-head .h-price{left:297px}.items-head .h-qty{left:417px}.items-head .h-total{left:490px}

.grand-total{left:317px;top:640px;width:357px;height:42px;background:var(--navy);color:var(--white);font-size:15px;font-weight:300}
.grand-total span{position:absolute;line-height:42px}
.section-title{font-size:15px;font-weight:400;line-height:20px}
.note{font-size:10px;color:var(--muted);line-height:13.5px}
.method-title{border-bottom:1px solid var(--navy);width:156px}
.sign-line{left:317px;top:752px;width:357px;height:2px;background:var(--navy)}
.sign-name{left:508px;top:765px;font-size:17px;letter-spacing:.5px;color:#333}

.contact-item{display:flex;align-items:center;gap:14px;font-size:11px;line-height:14px}
.contact-item svg{width:20px;height:20px;flex:none}

.services-band{left:0;top:895px;width:674px;height:68px;background:var(--navy)}
.services-band li{position:absolute;list-style:none;color:var(--white);font-size:14px;font-weight:300}

/* business cards */
.card{position:absolute;width:298px;height:190px;overflow:hidden;box-shadow:0 14px 30px rgba(10,40,90,.35)}
.card-front{left:820px;top:120px;background:var(--navy-deep)}
.card-front .white-side{position:absolute;left:0;top:0}
.card-front .owner{left:28px;top:38px;font-size:10px;color:var(--navy)}
.card-front .owner b{font-weight:700}
.card-contact{left:10px;font-size:9px;color:#333;display:flex;gap:8px;line-height:11px}
.card-contact svg{width:9px;height:9px;flex:none;margin-top:1px}
.card-front .brand-name{left:140px;width:148px;top:40px;font-size:17px;text-align:center}
.card-front .service{left:140px;width:148px;top:113px;font-size:13px;font-weight:500;color:var(--white);text-align:center}
.card-front .motto{left:140px;width:148px;top:143px;font-size:6px;color:var(--white);text-align:center}
.card-back{left:820px;top:340px;background:var(--navy-deep)}
.card-back .brand-name{left:0;width:298px;top:78px;font-size:30px;text-align:center}
</style>
</head>
<body>

<section class="invoice" aria-label="Invoice">
  <header class="invoice-header">
    <span class="brand-name">BELKAR RUG</span>
  </header>

  <div class="abs invoice-to">INVOICE TO:</div>
  <div class="abs invoice-badge">INVOICE</div>
  <div class="abs customer-bar"><span class="label">CUSTOMER</span><span class="number">N°: 000000000</span></div>
  <div class="abs customer-details">000 000 000<br>contact@example.com<br>Adderss, city</div>

  <div class="abs meta" style="left:504px;top:234px">Invoice</div>
  <div class="abs meta" style="left:572px;top:234px">: 00000</div>
  <div class="abs meta" style="left:446px;top:249px">Date</div>
  <div class="abs meta" style="left:514px;top:249px">: 01 February,2021</div>
  <div class="abs meta" style="left:446px;top:264px">Due Date</div>
  <div class="abs meta" style="left:514px;top:264px">: 01 February,2022</div>

  <div class="abs items-head">
    <span class="h-id">ID</span><span class="h-item">ITEMS</span><span class="h-price">UNIT PRICE</span><span class="h-qty">QTY</span><span class="h-total">TOTAL</span>
  </div>
  <div class="abs" style="left:0;top:368px;width:674px;height:238px">
    <div class="item-row" style="top:0"><span class="c-id">01</span><span class="c-item">Type of rug</span><span class="c-price">$ 00</span><span class="c-qty">1</span><span class="c-total">$ 00</span></div>
    <div class="item-row" style="top:34px"><span class="c-id">02</span><span class="c-item">Size</span><span class="c-price">$ 00</span><span class="c-qty">1</span><span class="c-total">$ 00</span></div>
    <div class="item-row" style="top:68px"><span class="c-id">03</span><span class="c-item">Background Color</span><span class="c-price">$ 00</span><span class="c-qty">1</span><span class="c-total">$ 00</span></div>
    <div class="item-row" style="top:102px"><span class="c-id">04</span><span class="c-item">Repair needs</span><span class="c-price">$ 00</span><span class="c-qty">1</span><span class="c-total">$ 00</span></div>
    <div class="item-row" style="top:136px"><span class="c-id">05</span><span class="c-item">Notes</span><span class="c-price">$ 00</span><span class="c-qty">1</span><span class="c-total">$ 00</span></div>
    <div class="item-row" style="top:170px"><span class="c-id">06</span><span class="c-item">Price</span><span class="c-price">$ 00</span><span class="c-qty">1</span><span class="c-total">$ 00</span></div>
    <div class="item-row" style="top:204px"><span class="c-id">07</span><span class="c-item">Rug cleaning disclaimer</span><span class="c-price">$ 00</span><span class="c-qty">1</span><span class="c-total">$ 00</span></div>
  </div>

  <div class="abs grand-total"><span style="left:18px">GRAND TOTAL</span><span style="left:245px">$ 00</span></div>

  <div class="abs section-title" style="left:58px;top:684px">PAYMENT CRITERIA</div>
  <div class="abs note" style="left:58px;top:707px">50% Advance, 50% After completion</div>
  <div class="abs section-title method-title" style="left:58px;top:734px">PAYMENT METHOD</div>
  <div class="abs note" style="left:58px;top:760px">Online Pay: info@belkarrug.com<br>CREDIT | DEBIT |<br>Cheques payments</div>

  <div class="abs sign-line"></div>
  <div class="abs sign-name">BELKAR RUG</div>

  <div class="abs contact-item" style="left:72px;top:852px">
    <svg viewBox="0 0 24 24" fill="none" stroke="#17294a" stroke-width="1.6"><path d="M12 22s7-7.5 7-13a7 7 0 0 0-14 0c0 5.5 7 13 7 13z"/><circle cx="12" cy="9" r="2.6"/></svg>
    <span>1420 Harwick Ave,<br>Elmridge, IL 60099</span>
  </div>
  <div class="abs contact-item" style="left:290px;top:852px">
    <svg viewBox="0 0 24 24" fill="#17294a"><path d="M6.6 10.8a15.1 15.1 0 0 0 6.6 6.6l2.2-2.2c.3-.3.7-.4 1-.2 1.1.4 2.3.6 3.6.6.6 0 1 .4 1 1V20c0 .6-.4 1-1 1A17 17 0 0 1 3 4c0-.6.4-1 1-1h3.5c.6 0 1 .4 1 1 0 1.2.2 2.4.6 3.6.1.3 0 .7-.2 1z"/></svg>
    <span>(555)014-2290<br>(555)014-2290</span>
  </div>
  <div class="abs contact-item" style="left:472px;top:852px">
    <svg viewBox="0 0 24 24" fill="none" stroke="#17294a" stroke-width="1.5"><circle cx="12" cy="12" r="9"/><ellipse cx="12" cy="12" rx="4" ry="9"/><path d="M3 12h18M4.5 7.5h15M4.5 16.5h15"/></svg>
    <span>info@belkarrug.com<br>www.belkarrug.com</span>
  </div>

  <ul class="abs services-band">
    <li style="left:34px;top:10px">▪ Antique Rug Repair</li>
    <li style="left:34px;top:31px">▪ Oriental Rug Restoration</li>
    <li style="left:250px;top:10px">▪ Antique Rug Cleaning</li>
    <li style="left:250px;top:31px">▪ Staircase Rug Installation</li>
    <li style="left:465px;top:10px">▪ Exemplary Customer Service</li>
    <li style="left:465px;top:31px">▪ Sun fade or Color Correction</li>
  </ul>
</section>

<section class="card card-front" aria-label="Business card front">
  <svg class="white-side" width="298" height="190" viewBox="0 0 298 190"><path d="M0 0H122C138 40 140 130 126 190H0z" fill="#fff"/></svg>
  <div class="abs owner"><b>Belkar</b> Rug</div>
  <div class="abs card-contact" style="top:99px">
    <svg viewBox="0 0 24 24" fill="#17294a"><path d="M6.6 10.8a15.1 15.1 0 0 0 6.6 6.6l2.2-2.2c.3-.3.7-.4 1-.2 1.1.4 2.3.6 3.6.6.6 0 1 .4 1 1V20c0 .6-.4 1-1 1A17 17 0 0 1 3 4c0-.6.4-1 1-1h3.5c.6 0 1 .4 1 1 0 1.2.2 2.4.6 3.6.1.3 0 .7-.2 1z"/></svg>
    <span>(555)014-2290</span>
  </div>
  <div class="abs card-contact" style="top:119px">
    <svg viewBox="0 0 24 24" fill="none" stroke="#17294a" stroke-width="2"><circle cx="12" cy="12" r="9"/><ellipse cx="12" cy="12" rx="4" ry="9"/><path d="M3 12h18"/></svg>
    <span>info@belkarrug.com</span>
  </div>
  <div class="abs card-contact" style="top:136px">
    <svg viewBox="0 0 24 24" fill="#17294a"><path d="M12 22s7-7.5 7-13a7 7 0 0 0-14 0c0 5.5 7 13 7 13z"/></svg>
    <span>1420 Harwick Ave,<br>Elmridge, IL 60099</span>
  </div>
  <div class="abs brand-name">BELKAR RUG</div>
  <div class="abs service">Oriental Rug Repair</div>
  <div class="abs motto">Authenticity and perfection.</div>
</section>

<section class="card card-back" aria-label="Business card back">
  <div class="abs brand-name">BELKAR RUG</div>
</section>

</body>
</html>
```